QV - menu design

Hi,

We require elegant menu design for upscale restaurant. Please find attached the logo and the menu items for your reference.

for inspiration, this is a good website: -
http://www.platewhisper.example/bellfoldnotes/about.php

We are very much open for Menu Size suggestions.

unfortunately the place is going under renovation, we don't have updated images to it. the closest look and feel to our place is http://varnelo.example ..

we are also open for creative options on the shape, the styles, etc. as long as it represents the fine dine feel ...

Thanks ...

Dear All,

We wouldlike to extend our apology for not being able to provide feedbacks on everysingle design. We were extremely busy and we have multiple contests opensimultaneously which makes the process even harder.

However,we would like to thank you all for the efforts you have put into designingour menu. It is very much appreciated …

We wishyou all success in your design ventures and we are quite positive that we willbe working with many of you on many projects in the soon future. 

Thanks & Regards,

TLG Team...

 

 

 

Industry/Entity Type

Restaurant

Requirements
Must have
• Please ensure that there are 'some' images in the menu ... this is very important.
Should not have
• IMPORTANT: -

1. Please DO NOT insert any currency sign to the menu
2. Please keep the prices of the menu at the end of the menu items descriptions NOT beside the menu item names. The font of the price should be similar to the menu item description and please DO NOT bold the numbers. the prices should be subtle.

Thank you ...

```html
<!DOCTYPE html>
<html lang="en">
<head>
<meta charset="utf-8">
<title>QV Café – Menu</title>
<link rel="stylesheet" href="https://fonts.googleapis.com/css2?family=Roboto+Condensed:wght@400;700&display=swap">
<style>
:root{
  --page:#ffffff;
  --paper:#f3f1ec;
  --paper-edge:#e6e1d7;
  --ink:#1c1c1c;
  --gold:#8c6a34;
  --tile-grey:#cdc7bc;
  --tile-grey-light:#d9d5cd;
  --cover-dark:#262220;
  --cover-brown:#7a4a1c;
  --cover-amber:#b87a34;
  --cover-text:#2a1a0c;
}
*{margin:0;padding:0;box-sizing:border-box}
html,body{width:1200px;height:927px;overflow:hidden;background:var(--page)}
body{position:relative;font-family:"Roboto Condensed",sans-serif;color:var(--ink)}

.inner-page{position:absolute;left:22px;top:22px;width:560px;height:883px;
  background:radial-gradient(ellipse at 40% 30%,#faf9f6 0%,var(--paper) 60%,var(--paper-edge) 100%)}
.section-title{position:absolute;left:53px;top:54px;font-size:50px;font-weight:400;color:var(--gold);letter-spacing:-.5px}
.dish{position:absolute;width:250px;font-size:14.5px;line-height:20px;white-space:nowrap}
.dish .price{display:block;font-size:18px;margin-top:8px;padding-left:2px}

.tile{position:absolute;width:126px;height:117px}
.photo{border-right:1px solid #fff;border-bottom:1px solid #fff}
.promo-text{position:absolute;left:48px;top:703px;font-size:19px;line-height:24px}
.ask-tile{background:var(--tile-grey)}
.ask-tile span{position:absolute;left:10px;top:30px;font-size:27px;line-height:34px;color:var(--gold)}
.brand-tile{background:var(--tile-grey-light);display:flex;align-items:center;justify-content:center;gap:8px}
.brand-tile .mark{width:12px;height:12px;border-radius:50%;background:#8d8a84}
.brand-tile .name{font-size:17px;letter-spacing:3px;color:#5a5853}

.cover{position:absolute;left:618px;top:18px;width:560px;height:887px;overflow:hidden;
  background:radial-gradient(ellipse 70% 55% at 50% 50%,var(--cover-amber) 0%,var(--cover-brown) 45%,#3a2817 80%,var(--cover-dark) 100%)}
.ornament-area{position:absolute;left:0;width:560px;height:140px;
  background:radial-gradient(ellipse 60% 60% at 50% 50%,rgba(200,160,80,.35) 0%,rgba(160,120,60,.18) 60%,transparent 100%)}
.ornament-area.top{top:70px}
.ornament-area.bottom{top:712px}
.cover-name{position:absolute;left:0;top:396px;width:560px;text-align:center;font-size:54px;font-weight:400;letter-spacing:16px;padding-left:16px;color:#1a1a1a}
.contact{position:absolute;left:0;top:580px;width:560px;text-align:center;font-size:13.5px;line-height:18.5px;color:var(--cover-text);font-style:normal}
</style>
</head>
<body>

<section class="inner-page" aria-label="First courses"></section>
<h1 class="section-title">First Courses</h1>

<p class="dish" style="left:54px;top:128px">Tagliatelle served on a whole Lobster<br>with fresh Asparagus tops, cherry<br>tomatoand crispy beef bacon.<span class="price">249</span></p>
<p class="dish" style="left:341px;top:131px">Whole wheat Maltagliati with<br>Porcini mushrooms and Parmesan<br>cheese cream.<span class="price">99</span></p>
<p class="dish" style="left:54px;top:247px">Penne pasta with fresh broccoli,<br>Taleggio cheese cream, toasted<br>almonds and fresh chili<span class="price" style="margin-top:12px">99</span></p>
<p class="dish" style="left:338px;top:247px">Spaghetti with a smooth and creamy<br>sauce and juicy chicken breast<span class="price" style="margin-top:32px">99</span></p>
<p class="dish" style="left:54px;top:361px">Fettuccinewith fresh salmon,<br>saffron and toasted pine nuts<span class="price" style="margin-top:12px">99</span></p>
<p class="dish" style="left:337px;top:361px">Seaweedtagliatelle with king<br>scallops and poached egg<span class="price" style="margin-top:12px">99</span></p>
<p class="dish" style="left:54px;top:453px">Risotto with Prawns, green peas<br>and beetroot reduction.<span class="price">149</span></p>
<p class="dish" style="left:335px;top:453px">Risotto “Primavera” with fresh<br>seasonal vegetables served on a<br>squash cream.<span class="price">69</span></p>
<p class="dish" style="left:54px;top:548px">Risotto with porcini mushrooms<br>and garlic chips<span class="price">00</span></p>

<div class="tile brand-tile" style="left:330px;top:553px"><span class="mark"></span><span class="name">QV Café</span></div>
<div class="tile photo" style="left:456px;top:553px;background:linear-gradient(135deg,#e9ece4,#c9473f 60%,#eef0e8)" role="img" aria-label="Photo of strawberry and mozzarella skewers on a plate"></div>

<p class="promo-text">Plate and dessert<br>of the day</p>
<div class="tile ask-tile" style="left:205px;top:670px"><span>Ask right<br>away</span></div>
<div class="tile photo" style="left:330px;top:670px;background:linear-gradient(135deg,#7a5c3c,#b68e62 50%,#d9c4a2)" role="img" aria-label="Photo of stuffed pastries with mushrooms"></div>
<div class="tile photo" style="left:456px;top:670px;background:linear-gradient(135deg,#f1ead8,#e6d8ae 50%,#4f8a3a)" role="img" aria-label="Photo of penne pasta with broccoli and chicken"></div>

<div class="tile photo" style="left:22px;top:787px;width:183px;height:118px;background:linear-gradient(135deg,#3a2a1c,#d9b97c 45%,#efe2c4)" role="img" aria-label="Photo of pasta with porcini mushrooms"></div>
<div class="tile photo" style="left:205px;top:787px;height:118px;background:linear-gradient(135deg,#d7a24a,#b84a2c 50%,#5c7a36)" role="img" aria-label="Photo of tagliatelle with vegetables"></div>
<div class="tile photo" style="left:330px;top:787px;height:118px;background:linear-gradient(135deg,#5a3d2a,#f4efe4 45%,#e9b53a 70%,#6b3a2c)" role="img" aria-label="Photo of a poached egg dish"></div>
<div class="tile photo" style="left:456px;top:787px;height:118px;background:linear-gradient(135deg,#f2f2ee,#8cb05a 50%,#5e8c38)" role="img" aria-label="Photo of risotto with green peas"></div>

<section class="cover" aria-label="Menu cover">
  <div class="ornament-area top" role="img" aria-label="Gold scroll ornament on a damask patterned background"></div>
  <p class="cover-name">QV CAFÉ</p>
  <address class="contact">
    Tel./Fax.: &nbsp;+30 21000 48315<br>
    Mobile: &nbsp;+30 6900 217 604<br>
    Email: info@qvcafe.example
  </address>
  <div class="ornament-area bottom" role="img" aria-label="Gold scroll ornament on a damask patterned background"></div>
</section>

</body>
</html>
```